Accounting practice seeks business card redesign with existing logo

Accounting practice has logo and slogan but more needs modern professional business revision. Must be in a file format ready to print quality business cards.

Open to artistic ideas but for the brand recognition the features below must be incorporated:

- Logo: attached in EPS format (Logo now blue)
- Slogan: Proven Business Solutions... That Work! (in orange legible handwriting type font)
- Name: Dorian T Felsham RBA AAT JP (letters in smaller font)
- Phone icon: 1800 593 817
- Mobile phone icon: 0488 614 752
- Web icon: www.velprasolutions.com.au
- Email icon: admin@velprasolutions.com.au
- See pics for dark blue/med blue line at bottom, this is a necessity.
- Globe that forms the 'dot' in the 'I' of Velpra is attached. It is too big at present.
- Rear side: pic attached. Note my logo is a watermark. I Will provide slightly revised wording details later. Please allow for a small white space at bottom of rear of card to write notes/appointment details.

I am open to ideas but must retain the above for brand recognition.

```html
<!DOCTYPE html>
<html lang="en">
<head>
<meta charset="utf-8">
<title>Velpra Solutions – Business Card</title>
<link rel="stylesheet" href="https://fonts.googleapis.com/css2?family=Roboto+Condensed:wght@400;700&family=Kaushan+Script&display=swap">
<style>
  :root {
    --stage: #dcdcdc;
    --navy: #1c2a6a;
    --navy-deep: #0f1c55;
    --mid-blue: #1f6fb4;
    --bar-blue: #2b86c9;
    --glow-blue: #1a5c9c;
    --orange: #f07f1a;
    --white: #ffffff;
    --ink: #1b1b1b;
  }
  * { box-sizing: border-box; margin: 0; padding: 0; }
  html, body { width: 1200px; height: 1011px; overflow: hidden; }
  body {
    background: var(--stage);
    font-family: "Roboto Condensed", Arial, sans-serif;
    display: flex;
    justify-content: center;
    align-items: center;
    gap: 90px;
  }
  .card {
    position: relative;
    width: 370px;
    height: 620px;
    overflow: hidden;
    box-shadow: 0 10px 24px rgba(0,0,0,.18);
  }

  /* Front */
  .card--front {
    background: radial-gradient(circle at 62% 58%, var(--glow-blue) 0%, #17407f 38%, var(--navy) 70%);
  }
  .brand {
    position: absolute; top: 86px; left: 0; right: 0;
    display: flex; justify-content: center; align-items: center; gap: 12px;
    color: var(--white);
  }
  .brand__dot {
    width: 26px; height: 26px; border-radius: 50%; background: var(--bar-blue); flex: none;
  }
  .brand__name {
    font-size: 40px; font-weight: 700; line-height: 1;
  }
  .slogan {
    position: absolute; top: 176px; left: 0; right: 0; text-align: center;
    font-family: "Kaushan Script", cursive; color: var(--orange); font-size: 22px;
  }
  .map-area {
    position: absolute; top: 250px; right: 44px; width: 70px; height: 62px;
    background: #17407f; border-radius: 10px;
  }
  .name-bar {
    position: absolute; top: 340px; left: 0; width: 300px; height: 44px;
    background: linear-gradient(90deg, var(--bar-blue), #2472b8);
    border-radius: 0 22px 22px 0;
    border: 2px solid rgba(255,255,255,.6); border-left: none;
    color: var(--white); display: flex; align-items: center; padding-left: 36px;
  }
  .name-bar__name { font-size: 22px; font-weight: 700; }
  .name-bar__letters { font-size: 12px; margin-left: 6px; }
  .contacts {
    position: absolute; top: 404px; left: 40px; list-style: none; color: var(--white);
  }
  .contacts li {
    display: flex; align-items: center; gap: 10px; font-size: 19px; margin-bottom: 8px;
  }
  .contacts svg { width: 16px; height: 16px; flex: none; }
  .base-band { position: absolute; left: 0; bottom: 0; width: 100%; height: 110px; }

  /* Back */
  .card--back { background: var(--white); }
  .back__panel {
    position: absolute; top: 0; left: 0; width: 100%; height: 458px; background: var(--navy);
    border-bottom: 5px solid var(--orange); padding: 30px 32px; color: var(--white);
  }
  .back__intro { font-size: 19px; font-weight: 700; line-height: 1.3; }
  .services { list-style: none; margin-top: 18px; }
  .services li {
    display: flex; align-items: center; gap: 14px; font-size: 19px; margin-bottom: 9px;
  }
  .services li::before {
    content: ""; width: 14px; height: 14px; border-radius: 50%;
    border: 3px solid var(--white); flex: none;
  }
  .notes { position: absolute; top: 488px; left: 32px; color: var(--ink); font-size: 15px; }
  .notes p { margin-bottom: 30px; }
</style>
</head>
<body>

<section class="card card--front">
  <div class="brand">
    <span class="brand__dot"></span>
    <span class="brand__name">Velpra Solutions</span>
  </div>
  <p class="slogan">Proven Business Solutions That Work!</p>
  <div class="map-area" role="img" aria-label="Outline map of Australia"></div>

  <div class="name-bar">
    <span class="name-bar__name">Dorian T Felsham</span>
    <span class="name-bar__letters">RCA RBA AAT JP</span>
  </div>

  <ul class="contacts">
    <li>
      <svg viewBox="0 0 16 16"><circle cx="8" cy="8" r="8" fill="#fff"/><path d="M5 4.5l1.6-.3.8 2-1 .8a5 5 0 0 0 2.6 2.6l.8-1 2 .8-.3 1.6c-3.6.3-6.8-2.9-6.5-6.5z" fill="#1c2a6a"/></svg>
      1800 593 817
    </li>
    <li>
      <svg viewBox="0 0 16 16"><circle cx="8" cy="8" r="8" fill="#fff"/><rect x="5.5" y="3.5" width="5" height="9" rx="1" fill="#1c2a6a"/><rect x="6.5" y="4.8" width="3" height="5.5" fill="#fff"/></svg>
      0488 614 752
    </li>
    <li>
      <svg viewBox="0 0 16 16"><rect x="1" y="3" width="14" height="10" fill="#fff"/><path d="M1 3l7 6 7-6" fill="none" stroke="#1c2a6a" stroke-width="1.3"/></svg>
      admin@velprasolutions.com.au
    </li>
    <li>
      <svg viewBox="0 0 16 16"><circle cx="8" cy="8" r="7" fill="#fff"/><path d="M1 8h14M8 1c-3 3.5-3 10.5 0 14M8 1c3 3.5 3 10.5 0 14" fill="none" stroke="#1c2a6a" stroke-width="1"/></svg>
      www.velprasolutions.com.au
    </li>
  </ul>

  <svg class="base-band" viewBox="0 0 370 110" preserveAspectRatio="none" aria-hidden="true">
    <polygon points="0,70 370,10 370,110 0,110" fill="#1f6fb4"/>
    <polygon points="260,28 370,10 370,110 220,110" fill="#0f1c55"/>
    <line x1="0" y1="70" x2="370" y2="10" stroke="#ffffff" stroke-width="2"/>
  </svg>
</section>

<section class="card card--back">
  <div class="back__panel">
    <p class="back__intro">Your trusted provider of quality business and accounting solutions, proven to work for small to medium business and tradies.</p>
    <ul class="services">
      <li>Bookkeeping</li>
      <li>Accounting</li>
      <li>Taxation</li>
      <li>Business Advice</li>
      <li>Debt Recovery</li>
      <li>ATO Assistance</li>
      <li>Business Start Up</li>
      <li>Accounting Software</li>
    </ul>
  </div>
  <div class="notes">
    <p>Notes:</p>
    <p>Appointment Details:</p>
  </div>
</section>

</body>
</html>
```